Business Card and Letterhead Design for Public Accounting Firm

Business card and letterhead design for a CPA Firm located in Orange County, CA. We're looking for a modern and professional design utilizing our existing logo. We'd like a clean "less is more" look, but also something that catches the eye. We provide a high level of service to our clients. Open to single or double sided business cards.

Additional info: color numbers on logo
Blue :
R 0
G 83
B 125

#00537D

Silver :

R 154
G 154
B 154

#9A9A9A

Target Market(s)

Businesses and individuals

Industry/Entity Type

Accounting

Contact Information for Business Card

Moss Whitfield & Danby LLP - 4827 Larkspur Vale Road, Irvine, CA 92614 - (949)731-2864 - mwdaccts.example

Font styles to use
Serif
Sans Serif
Other font styles liked:
• See font file uploaded

Colors
0054AA
0677BA
7BADD7
CADEEF
E8F1F8

Requirements
Nice to have
• Possibly use the font file provided which matches our logo, but adjust to be not in all caps

```html
<!DOCTYPE html>
<html lang="en">
<head>
<meta charset="utf-8">
<title>Moss Whitfield &amp; Danby LLP — Business Card</title>
<link rel="stylesheet" href="https://fonts.googleapis.com/css2?family=EB+Garamond:wght@400;500&display=swap">
<style>
  :root {
    --backdrop: #2e2e2f;
    --card: #f7f7f7;
    --brand-blue: #00537d;
    --brand-silver: #9a9a9a;
    --ink: #333333;
    --rule: #c4c4c4;
  }
  * { margin: 0; padding: 0; box-sizing: border-box; }
  html, body {
    width: 1200px; height: 900px; overflow: hidden;
    background: var(--backdrop);
    font-family: "EB Garamond", Georgia, serif;
  }
  .canvas {
    position: relative; width: 1200px; height: 900px;
    display: flex; flex-direction: column; align-items: center; justify-content: center; gap: 44px;
  }
  .card {
    position: relative; width: 600px; height: 343px;
    background: linear-gradient(135deg, #ffffff 0%, var(--card) 60%, #ececec 100%);
    box-shadow: 0 10px 24px rgba(0,0,0,.45);
  }
  .wordmark {
    position: absolute; display: flex; align-items: center; gap: 14px;
  }
  .wordmark__square {
    width: 22px; height: 22px; background: var(--brand-blue); flex: none;
  }
  .wordmark__name {
    color: var(--brand-silver); font-weight: 400; font-size: 24px;
    letter-spacing: 2px; text-transform: uppercase; line-height: 1.05;
    padding-left: 14px; border-left: 1px solid var(--rule);
  }
  .card--front .wordmark { left: 230px; top: 190px; }
  .card--back .wordmark { left: 44px; top: 40px; }
  .rule { position: absolute; height: 1px; background: var(--rule); }
  .rule--top { left: 44px; right: 44px; top: 112px; }
  .rule--bottom { left: 44px; right: 44px; top: 262px; }
  .firm-name {
    position: absolute; left: 110px; top: 204px;
    color: var(--brand-blue); font-size: 21px; font-weight: 500;
    font-variant: small-caps; letter-spacing: 1.5px; white-space: nowrap;
  }
  .address {
    position: absolute; right: 44px; top: 134px; text-align: right;
    color: var(--ink); font-size: 17px; line-height: 1.35; font-style: normal;
  }
  .address__line { display: flex; align-items: center; justify-content: flex-end; gap: 6px; }
  .contact { position: absolute; left: 44px; top: 276px; color: var(--ink); font-size: 16px; }
  .contact__item { display: flex; align-items: center; gap: 8px; line-height: 1.6; }
  .icon { width: 13px; height: 13px; flex: none; }
</style>
</head>
<body>
<main class="canvas">
  <section class="card card--front" aria-label="Business card front">
    <div class="wordmark">
      <span class="wordmark__square"></span>
      <span class="wordmark__name">Moss Whitfield<br>&amp; Danby LLP</span>
    </div>
  </section>

  <section class="card card--back" aria-label="Business card back">
    <div class="wordmark">
      <span class="wordmark__square"></span>
      <span class="wordmark__name">Moss Whitfield<br>&amp; Danby LLP</span>
    </div>
    <div class="rule rule--top"></div>
    <address class="address">
      <span class="address__line">4827 Larkspur Vale Road
        <svg class="icon" viewBox="0 0 12 16" aria-hidden="true"><path d="M6 0a6 6 0 0 0-6 6c0 4.5 6 10 6 10s6-5.5 6-10a6 6 0 0 0-6-6zm0 8.5A2.5 2.5 0 1 1 6 3.5a2.5 2.5 0 0 1 0 5z" fill="var(--brand-blue)"/></svg>
      </span>
      <span class="address__line">Irvine, CA 92614</span>
    </address>
    <p class="firm-name">Moss Whitfield &amp; Danby LLP</p>
    <div class="rule rule--bottom"></div>
    <div class="contact">
      <p class="contact__item">
        <svg class="icon" viewBox="0 0 16 16" aria-hidden="true"><path d="M3 1h3l1.5 4-2 1.3a9 9 0 0 0 4.2 4.2L11 8.5l4 1.5v3a2 2 0 0 1-2 2A12 12 0 0 1 1 3a2 2 0 0 1 2-2z" fill="var(--brand-blue)"/></svg>
        (949)731-2864
      </p>
      <p class="contact__item">
        <svg class="icon" viewBox="0 0 16 16" aria-hidden="true"><circle cx="8" cy="8" r="6.5" fill="none" stroke="var(--brand-blue)" stroke-width="1.6"/><path d="M1.5 8h13M8 1.5c-3 3.5-3 9.5 0 13M8 1.5c3 3.5 3 9.5 0 13" fill="none" stroke="var(--brand-blue)" stroke-width="1.2"/></svg>
        www.mwdaccts.example
      </p>
    </div>
  </section>
</main>
</body>
</html>
```